Professional and modern website for Real Estate services company

Hi there! We're looking for a responsive, highly professional and modern (in line with Latest trends) coded website for a Real Estate services company named Portales720º (find logo attached). I will try to Explain how I picture it in my head, but feel free to step out of the script and design it as you please. The structure for the website must be as Follows: - Menu: at the top of the screen, always visible (in any page and when to scrolling down). Logo at the left hand side (clicking redirects to home), then a Services, About us, Blog and Contact and on the right hand, Estimate and Log in (just placeholder, no log in required yet). - Home: (I like https://fr.velmora.example/): a landscape picture of Madrid's skyline. Very important That at a first glance (without scrolling) you can see a box to input data of your building to get an estimate (Post code, Number of homes, Number of garages, Number of stores, Swimming pool (yes / no) Concierge (yes / no)). Should there be a small space Also for a corporate presentation video (more or less like https://www.bravunecasales.example/ but With the estimate Request box INSTEAD OF the App - however, do not take this one as example Given I just wanted to illustrate the structure). Still in the Home, bellow the first glance, I'd like to have a brief introduction of the following pages (Services, About us, Blog and Contact). This can be in a Either "square" form (like https://fr.velmora.example/) or in a "scroll" form (like https://k7portales.example/). - Services: we offer 3 sets of services, each of them composed by three specific services, Namely: * Administration Treasury Accounting Savings * Consulting Legal Technical Regulatory * Mediation Repairs Meetings Delinquency For the sake of structuring, each of the nine services will Have to written description composed of 3 small paragraphs of About 15 words. I Tend to like to Accompany With each of the services related icons / vectors, but feel free to design them as you want. - About us: content not yet defined, but will be a series of bullets / sections in Which We talk about prep or differentiating points. We can include the corporate video presentation here again. - Blog: just a space Where you can see to the blog entries (in Home, probably just show 3/4). - Contact: a fancy contact form, with map, address, telephone, e-mail and opening hours. Just to give it a bit more content, maybe include a catch phrase like "We're looking forward to meeting you!" or something like that. - Estimate: this is the Most Important page in the website (in Addition to the upper part of the Home page). Basically replicate the estimate for the home box, but maybe with a bit more design or extended, Given this is a single page just for that. - Log in: opens a drop-down with user and password (just placeholder, no log in required yet). Regarding colors, we still do not Have a color scheme, so anything in line With the logo is OK. Many thanks in advance, Martin

Target Market(s)

All ages and genders

Industry/Entity Type

Real Estate

Coding

Coded - Design and coding required

Number of Pages Required

5+ page

Font styles to use
Sans Serif

Requirements
Must have
• Blank colored background

```html
<!DOCTYPE html>
<html lang="en">
<head>
<meta charset="utf-8">
<title>Portales 720 – Real Estate Services</title>
<link href="https://fonts.googleapis.com/css2?family=Montserrat:wght@600;700&family=Roboto:wght@400;500;700&family=Open+Sans:wght@400;600&display=swap" rel="stylesheet">
<style>
:root{
  --orange:#c8650a;
  --orange-dark:#b45a08;
  --ink:#222222;
  --text:#555555;
  --grey-band:#ebebeb;
  --dark-circle:#555555;
  --footer:#232323;
  --white:#ffffff;
  --line:#d9d9d9;
}
*{box-sizing:border-box;margin:0;padding:0}
html,body{width:1200px;height:3147px;overflow:hidden;background:var(--white)}
body{position:relative;font-family:'Open Sans',Arial,sans-serif;color:var(--text)}
.abs{position:absolute}
a{color:inherit;text-decoration:none}

/* header */
.site-header{position:absolute;left:0;top:0;width:1200px;height:137px;background:var(--white)}
.brand{position:absolute;left:98px;top:40px;display:flex;align-items:center;gap:10px;font-family:'Roboto',sans-serif;font-weight:700;font-size:44px;color:#3a3a3a;letter-spacing:-1px}
.brand-dot{width:14px;height:14px;background:var(--orange);border-radius:50%}
.top-actions{position:absolute;right:100px;top:24px;display:flex;align-items:center;gap:16px;font-family:'Roboto',sans-serif;font-size:15px;color:#333}
.phone{display:flex;align-items:center;gap:8px}
.phone-icon{width:28px;height:28px;border-radius:50%;background:#333;display:flex;align-items:center;justify-content:center}
.btn-estimate{background:var(--orange);color:#fff;font-weight:500;padding:9px 14px;font-size:14px}
.btn-login{border:2px solid #333;padding:7px 26px;font-size:14px;font-weight:500;border-radius:2px}
.main-nav{position:absolute;right:98px;top:88px;display:flex;gap:36px;font-family:'Roboto',sans-serif;font-size:16px;font-weight:500;color:#222}
.main-nav .active{color:var(--orange);border:2px solid var(--orange);border-top:none;padding:0 8px 4px;position:relative}

/* hero */
.hero{position:absolute;left:0;top:137px;width:1200px;height:413px;background:linear-gradient(180deg,#d9dde0 0%,#b7bdc2 45%,#6f7479 100%)}
.hero-title{position:absolute;left:0;width:1200px;top:92px;text-align:center;font-family:'Montserrat',sans-serif;font-weight:700;font-size:46px;color:var(--orange)}
.hero-text{position:absolute;left:210px;width:780px;top:170px;text-align:center;font-size:15px;line-height:26px;color:#333}
.hero-arrow{position:absolute;top:180px}

/* estimate band */
.estimate-band{position:absolute;left:0;top:550px;width:1200px;height:160px;background:var(--orange)}
.field{position:absolute;width:206px;height:38px;border:1.5px solid #f1cfa9;color:#fbe8d4;font-size:15px;padding:8px 9px}
.option{position:absolute;font-family:'Roboto',sans-serif;font-size:15px;color:#fff;display:flex;align-items:center;gap:8px}
.option b{font-weight:700}
.radio{width:14px;height:14px;border:1.5px solid #fff;border-radius:50%;display:inline-block;position:relative}
.radio.on::after{content:"";position:absolute;left:2.5px;top:2.5px;width:6px;height:6px;background:#fff;border-radius:50%}
.btn-submit{position:absolute;left:591px;top:634px;width:146px;height:38px;background:#555;color:#fff;font-size:15px;text-align:center;line-height:36px;border:1px solid #777}

/* about */
.section-title{font-family:'Montserrat',sans-serif;font-weight:700;color:var(--orange);font-size:30px}
.about-title{position:absolute;left:98px;top:746px}
.rule{position:absolute;height:2px;background:var(--orange)}
.about-copy{position:absolute;left:98px;width:572px;font-size:13px;line-height:23px;color:#444}
.btn-orange{position:absolute;background:var(--orange);color:#fff;font-size:14px;font-weight:600;text-align:center}
.video{position:absolute;left:700px;top:772px;width:402px;height:283px;border:4px solid #fff;box-shadow:0 0 6px rgba(0,0,0,.25);background:linear-gradient(135deg,#c9c2b8,#8c8f94 60%,#5d6470)}
.video-bar{position:absolute;left:14px;right:14px;bottom:14px;height:6px;background:rgba(255,255,255,.4)}
.video-bar span{display:block;width:48%;height:100%;background:#4a90c8}

/* services */
.services{position:absolute;left:0;top:1118px;width:1200px;height:694px;background:var(--grey-band)}
.center-title{position:absolute;left:0;width:1200px;text-align:center}
.intro{position:absolute;left:150px;width:900px;text-align:center;font-size:13px;line-height:25px;color:#444}
.service-name{position:absolute;width:260px;text-align:center;font-family:'Roboto',sans-serif;font-weight:500;font-size:18px}
.service-list{position:absolute;width:260px;list-style:none;text-align:center;font-size:15px;line-height:26px;color:#444}
.service-list li::before{content:"";display:inline-block;width:9px;height:9px;border:2px solid #333;border-radius:50%;margin-right:8px;vertical-align:0}
.btn-outline{position:absolute;border:2px solid #333;background:#fff;color:#222;font-size:14px;text-align:center;border-radius:2px}

/* blog */
.post-img{position:absolute;top:1932px;width:319px;height:228px}
.date{position:absolute;width:58px;height:58px;color:#fff;font-family:'Roboto',sans-serif;font-size:15px;font-weight:500;text-align:center;line-height:22px;padding-top:7px}
.post-title{position:absolute;width:319px;text-align:center;font-family:'Roboto',sans-serif;font-size:18px;color:#222;top:2182px}
.post-text{position:absolute;width:319px;text-align:center;font-size:12px;line-height:20px;color:#555;top:2218px}

/* map */
.map{position:absolute;left:0;top:2403px;width:1200px;height:337px;background:linear-gradient(135deg,#e9e6df 0%,#dedbd3 50%,#d2e2c8 100%);border-top:3px solid var(--orange)}
.address-card{position:absolute;left:497px;top:2518px;width:258px;height:140px;background:#fff;box-shadow:0 1px 6px rgba(0,0,0,.25);padding:22px 18px 0 58px;font-family:'Roboto',sans-serif}
.address-card h4{font-size:16px;font-weight:700;color:#222;margin-bottom:10px}
.address-card p{font-size:14px;line-height:24px;color:#222}

/* footer */
.site-footer{position:absolute;left:0;top:2740px;width:1200px;height:407px;background:var(--footer);color:#fff;font-family:'Roboto',sans-serif}
.foot-brand{position:absolute;left:98px;top:54px;font-size:38px;font-weight:700;letter-spacing:-1px;display:flex;align-items:center;gap:8px}
.foot-brand i{width:12px;height:12px;border-radius:50%;background:#fff;display:block}
.foot-hours{position:absolute;left:98px;top:130px;font-size:14px;line-height:26px}
.foot-head{position:absolute;top:48px;font-size:17px;font-weight:500;letter-spacing:.5px}
.foot-rule{position:absolute;top:80px;width:104px;height:2px;background:#fff}
.quick-links{position:absolute;left:384px;top:100px;list-style:none;font-size:14px;line-height:32px}
.quick-links li::before{content:"› ";}
.contact-item{position:absolute;left:543px;display:flex;gap:20px;font-size:13px;line-height:21px}
.contact-item .ic{width:34px;height:34px;border:1.5px solid #fff;border-radius:50%;flex:none;display:flex;align-items:center;justify-content:center}
.contact-item b{font-weight:700;font-size:14px}
.f-input{position:absolute;border:1.5px solid #bbb;border-radius:3px;font-size:12px;color:#ddd;padding:8px 10px}
.btn-send{position:absolute;left:812px;top:2955px;width:120px;height:36px;background:var(--orange);color:#fff;font-size:12px;text-align:center;line-height:36px}
.foot-line{position:absolute;left:98px;top:325px;width:1004px;height:1px;background:#555}
.copyright{position:absolute;left:98px;top:353px;font-size:13px;font-weight:500}
.socials{position:absolute;right:110px;top:340px;display:flex;gap:8px}
.socials span{width:32px;height:32px;border:1.5px solid #fff;border-radius:50%;display:block}
</style>
</head>
<body>

<header class="site-header">
  <a class="brand" href="#"><span>portales720</span><span class="brand-dot"></span></a>
  <div class="top-actions">
    <span class="phone"><span class="phone-icon"><svg width="14" height="14" viewBox="0 0 24 24"><path fill="#fff" d="M6.6 10.8a15 15 0 006.6 6.6l2.2-2.2c.3-.3.7-.4 1-.2 1.1.4 2.3.6 3.6.6.6 0 1 .4 1 1V20c0 .6-.4 1-1 1A17 17 0 013 4c0-.6.4-1 1-1h3.5c.6 0 1 .4 1 1 0 1.3.2 2.5.6 3.6.1.3 0 .7-.2 1z"/></svg></span>180 047 9183</span>
    <a class="btn-estimate" href="#">ESTIMATE</a>
    <a class="btn-login" href="#">LOGIN</a>
  </div>
  <nav class="main-nav">
    <a class="active" href="#">HOME</a>
    <a href="#">SERVICES</a>
    <a href="#">ABOUT US</a>
    <a href="#">BLOG</a>
    <a href="#">CONTACT</a>
  </nav>
</header>

<section class="hero" role="img" aria-label="City skyline photograph with skyscrapers under a hazy sky">
  <h1 class="hero-title">WELCOME TO PORTALES 720</h1>
  <p class="hero-text">Nemo enim ipsam voluptatem quia voluptas sit aspernatur aut odit aut fugit, sed quia consequuntur magni dolores eos qui ratione voluptatem</p>
  <svg class="hero-arrow" style="left:32px" width="24" height="44" viewBox="0 0 24 44"><path d="M22 2L2 22l20 20" fill="none" stroke="#fff" stroke-width="2"/></svg>
  <svg class="hero-arrow" style="left:1144px" width="24" height="44" viewBox="0 0 24 44"><path d="M2 2l20 20L2 42" fill="none" stroke="#fff" stroke-width="2"/></svg>
</section>

<section class="estimate-band">
  <div class="field" style="left:138px;top:33px">Post code</div>
  <div class="field" style="left:360px;top:33px">Number of homes</div>
  <div class="field" style="left:138px;top:84px">Number of garages</div>
  <div class="field" style="left:360px;top:84px">Number of stores</div>
  <div class="option" style="left:591px;top:42px"><b>Swimming pool:</b><span class="radio on"></span>Yes<span class="radio"></span>No</div>
  <div class="option" style="left:862px;top:42px"><b>Concierge:</b><span class="radio on"></span>Yes<span class="radio"></span>No</div>
</section>
<div class="btn-submit">Estimate Now</div>

<h2 class="section-title about-title">About Portales 720</h2>
<div class="rule" style="left:98px;top:790px;width:182px"></div>
<p class="about-copy" style="top:812px">Nemo enim ipsam voluptatem quia voluptas sit aspernatur aut odit aut fugit, sed quia conse quuntur magni dolores eos qui ratione voluptatem sequi nesciunt. Neque porro quisquam est, qui dolorem ipsum quia dolor sit amet, consectetur, adipisci velit, sed quia non numquam eius modi tempora incidunt ut labore et dolore magnam aliquam quaerat voluptatem.</p>
<p class="about-copy" style="top:912px">Exercitationem ullam corporis suscipit laboriosam, nisi ut aliquid ex ea commodi consequatur? Quis autem vel eum iure reprehenderit qui in ea voluptate velit esse quam nihil molestiae con sequatur, vel illum qui dolorem eum fugiat quo voluptas nulla pariatur.</p>
<a class="btn-orange" href="#" style="left:98px;top:1012px;width:116px;height:42px;line-height:42px">Read More</a>
<div class="video" role="img" aria-label="Corporate presentation video still: an agent showing a tablet to a couple outside a building">
  <svg style="position:absolute;left:165px;top:104px" width="62" height="62" viewBox="0 0 62 62"><circle cx="31" cy="31" r="28" fill="rgba(0,0,0,.35)" stroke="#fff" stroke-width="3"/><path d="M24 18l20 13-20 13z" fill="#fff"/></svg>
  <div class="video-bar"><span></span></div>
</div>

<section class="services">
  <h2 class="section-title center-title" style="top:38px">Our Services</h2>
  <p class="intro" style="top:94px">Nemo enim ipsam voluptatem quia voluptas sit aspernatur aut odit aut fugit, sed quia consequuntur magni dolores eos qui ratione voluptatem sequi nesciunt.</p>
  <svg class="abs" style="left:0;top:160px" width="1200" height="250" viewBox="0 0 1200 250">
    <path d="M380 92 Q450 112 520 92 L520 158 Q450 138 380 158Z" fill="#555"/>
    <path d="M680 92 Q750 112 820 92 L820 158 Q750 138 680 158Z" fill="#555"/>
    <path d="M440 114l26 11-26 11 6-11z" fill="#fff"/>
    <path d="M732 114l26 11-26 11 6-11z" fill="#fff"/>
    <circle cx="302" cy="125" r="118" fill="var(--orange)"/>
    <circle cx="302" cy="125" r="106" fill="none" stroke="#fff" stroke-width="3"/>
    <circle cx="600" cy="125" r="118" fill="var(--dark-circle)"/>
    <circle cx="600" cy="125" r="106" fill="none" stroke="#fff" stroke-width="3"/>
    <circle cx="894" cy="125" r="118" fill="var(--orange)"/>
    <circle cx="894" cy="125" r="106" fill="none" stroke="#fff" stroke-width="3"/>
    <!-- house -->
    <g fill="none" stroke="#fff" stroke-width="7" stroke-linejoin="round">
      <path d="M258 128l44-40 44 40"/>
      <path d="M270 118v46h64v-46"/>
    </g>
    <rect x="290" y="122" width="22" height="20" fill="none" stroke="#fff" stroke-width="5"/>
    <path d="M301 122v20M290 132h22" stroke="#fff" stroke-width="3"/>
    <!-- headset -->
    <g fill="none" stroke="#fff" stroke-width="7" stroke-linecap="round">
      <path d="M566 128a34 34 0 0168 0"/>
      <path d="M628 150q-6 20-28 20"/>
    </g>
    <rect x="558" y="122" width="16" height="32" rx="6" fill="#fff"/>
    <rect x="626" y="122" width="16" height="32" rx="6" fill="#fff"/>
    <circle cx="597" cy="170" r="6" fill="#fff"/>
    <!-- building -->
    <g fill="none" stroke="#fff" stroke-width="6">
      <path d="M858 170V96l46-16v90"/>
      <path d="M904 110h26v60"/>
      <path d="M850 170h88"/>
    </g>
    <g fill="#fff">
      <rect x="868" y="106" width="10" height="12"/><rect x="886" y="106" width="10" height="12"/>
      <rect x="868" y="126" width="10" height="12"/><rect x="886" y="126" width="10" height="12"/>
      <rect x="868" y="146" width="10" height="12"/><rect x="886" y="146" width="10" height="12"/>
      <rect x="912" y="122" width="10" height="10"/><rect x="912" y="142" width="10" height="10"/>
    </g>
  </svg>
  <h3 class="service-name" style="left:172px;top:454px;color:var(--orange)">ADMINISTRATION</h3>
  <h3 class="service-name" style="left:470px;top:454px;color:#333">CONSULTING</h3>
  <h3 class="service-name" style="left:764px;top:454px;color:var(--orange)">MEDIATION</h3>
  <ul class="service-list" style="left:172px;top:494px"><li>Treasury</li><li>Accounting</li><li>Savings</li></ul>
  <ul class="service-list" style="left:470px;top:494px"><li>Legal</li><li>Technical</li><li>Regulatory</li></ul>
  <ul class="service-list" style="left:764px;top:494px"><li>Repairs</li><li>Meetings</li><li>Delinquency</li></ul>
  <a class="btn-outline" href="#" style="left:241px;top:596px;width:128px;height:42px;line-height:38px">Find Out More</a>
  <a class="btn-outline" href="#" style="left:536px;top:596px;width:128px;height:42px;line-height:38px">Find Out More</a>
  <a class="btn-outline" href="#" style="left:830px;top:596px;width:128px;height:42px;line-height:38px">Find Out More</a>
</section>

<h2 class="section-title center-title" style="top:1840px">Our Blog Posts</h2>
<div class="rule" style="left:540px;top:1890px;width:120px"></div>

<div class="post-img" style="left:98px;background:linear-gradient(135deg,#56708a,#9fb0bf 55%,#e9ecef)" role="img" aria-label="Photo of a handshake with a small model house"></div>
<div class="post-img" style="left:441px;background:linear-gradient(180deg,#8fb3d4,#5b7ea3 60%,#3b4e66)" role="img" aria-label="Photo of a man looking up at tall glass towers"></div>
<div class="post-img" style="left:783px;background:linear-gradient(200deg,#f5d48a,#c98a3a 45%,#4c3a28)" role="img" aria-label="Photo of skyscrapers at sunset with a plane overhead"></div>
<div class="date" style="left:98px;top:2102px;background:var(--orange)">AUG<br>11</div>
<div class="date" style="left:441px;top:2102px;background:#333">AUG<br>20</div>
<div class="date" style="left:783px;top:2102px;background:#333">AUG<br>20</div>

<h3 class="post-title" style="left:98px">Nemo enim ipsam voluptatem</h3>
<h3 class="post-title" style="left:441px">Perspiciatis unde omnis</h3>
<h3 class="post-title" style="left:783px">Totam rem aperiam</h3>
<p class="post-text" style="left:98px">Sed ut perspiciatis unde omnis iste natus error sit voluptatem accusantium doloremque laudantium, totam rem aperiam, eaque ipsam.</p>
<p class="post-text" style="left:441px">Sed ut perspiciatis unde omnis iste natus error sit voluptatem accusantium doloremque laudantium, totam rem aperiam, eaque ipsam.</p>
<p class="post-text" style="left:783px">Sed ut perspiciatis unde omnis iste natus error sit voluptatem accusantium doloremque laudantium, totam rem aperiam, eaque ipsam.</p>
<a class="btn-orange" href="#" style="left:197px;top:2308px;width:122px;height:40px;line-height:40px;font-weight:500">Read More</a>
<a class="btn-outline" href="#" style="left:540px;top:2308px;width:122px;height:40px;line-height:36px">Read More</a>
<a class="btn-outline" href="#" style="left:880px;top:2308px;width:122px;height:40px;line-height:36px">Read More</a>

<div class="map" role="img" aria-label="Street map of the area around the office, with roads, a lake and a park"></div>
<div class="address-card">
  <svg style="position:absolute;left:24px;top:22px" width="20" height="28" viewBox="0 0 20 28"><path d="M10 0a10 10 0 0110 10c0 7-10 18-10 18S0 17 0 10A10 10 0 0110 0z" fill="#d23b2b"/><circle cx="10" cy="10" r="4" fill="#fff"/></svg>
  <h4>OFFICE ADDRESS</h4>
  <p>482 Alder Grove Lane,<br>Fairhaven, 90417</p>
</div>

<footer class="site-footer">
  <div class="foot-brand"><span>portales720</span><i></i></div>
  <div class="foot-hours"><b style="font-size:15px">Opening Hours:</b><br>Mon - Fri: 10.00 A.M - 6.00P.M<br>Saturday &amp; Sunday Closed</div>

  <h4 class="foot-head" style="left:384px">QUICK LINKS</h4>
  <div class="foot-rule" style="left:384px"></div>
  <ul class="quick-links"><li>Home</li><li>About Us</li><li>Services</li><li>Blog</li><li>Contact Us</li></ul>

  <h4 class="foot-head" style="left:543px">CONTACT US</h4>
  <div class="foot-rule" style="left:543px"></div>
  <div class="contact-item" style="top:104px"><span class="ic"><svg width="12" height="16" viewBox="0 0 20 28"><path d="M10 0a10 10 0 0110 10c0 7-10 18-10 18S0 17 0 10A10 10 0 0110 0z" fill="#fff"/></svg></span><div><b>LOCAL CONTRACTORS,</b><br>482 Alder Grove Lane,<br>Fairhaven, 90417</div></div>
  <div class="contact-item" style="top:180px"><span class="ic"><svg width="10" height="16" viewBox="0 0 10 16"><rect x="1" y="1" width="8" height="14" rx="1.5" fill="none" stroke="#fff" stroke-width="1.5"/></svg></span><div><b>PHONE:</b><br>180 047 9183</div></div>
  <div class="contact-item" style="top:240px"><span class="ic"><svg width="14" height="10" viewBox="0 0 14 10"><rect width="14" height="10" fill="#fff"/><path d="M0 0l7 6 7-6" fill="none" stroke="#232323" stroke-width="1.3"/></svg></span><div><b>Mail:</b><br>info@portales720.example</div></div>

  <h4 class="foot-head" style="left:812px">CONTACT FORM</h4>
  <div class="foot-rule" style="left:812px"></div>
  <div class="f-input" style="left:812px;top:95px;width:140px;height:36px">Name</div>
  <div class="f-input" style="left:960px;top:95px;width:140px;height:36px">Phone</div>
  <div class="f-input" style="left:812px;top:140px;width:288px;height:66px">Message</div>
  <div class="foot-line"></div>
  <div class="copyright">Copyright © 2016 Portales 720. All Right Reserved</div>
  <div class="socials"><span></span><span></span><span></span><span></span><span></span></div>
</footer>
<div class="btn-send">SEND MESSAGE</div>

</body>
</html>
```